Corvane Hollis Landing Page

We need a landing page re-designed for a new website www.corvanehollis.com and the website is live if you search the address provided.
We need the industry standard files for embedding this into the landing page of our website. The company is a real estate advisory firm, we provide professional property services and are focused on business rates (commercial property taxation in the UK).
We have uploaded a file which is meant to provide a visual guide as to how we envisage the landing page looking. You are free to come up with an entirely different creative design. The image at the top with the search button is taken from another website so the design will need to be distinctly different but may follow the same theme. Furthermore, the colour palette does not need to be followed slavishly and can be modified changed and improved upon. It might be that you want to incorporate other visual cues such as a desktop PC, laptop and Vexa as these are devices the website will be accessed from; however, this is not essential and only a guide.
**To clarify, please note, the target industry is commercial properties and not residential or domestic property, so please when incorporating designs of buildings its important to focus on commercial property such as shops, offices, industrial buildings etc.**
Occupiers of commercial real estate in the UK who pay property tax to occupy the property.

```html
<!DOCTYPE html>
<html lang="en">
<head>
<meta charset="utf-8">
<title>Corvane Hollis – Business Rates Valuations</title>
<link rel="stylesheet" href="https://fonts.googleapis.com/css2?family=Roboto:wght@400;500;700&display=swap">
<style>
:root{
  --navy:#0d2451;
  --orange:#f5520c;
  --ink:#333a44;
  --muted:#5b6270;
  --band:#eff4fb;
  --line:#d9dee6;
  --backdrop:#ececec;
}
*{box-sizing:border-box;margin:0;padding:0}
html,body{width:1200px;height:1200px;overflow:hidden;background:var(--backdrop);font-family:"Roboto",Arial,sans-serif;color:var(--ink)}
.page{position:absolute;left:249px;top:0;width:1030px;height:1762px;background:#fff;transform:scale(0.681);transform-origin:0 0}
.abs{position:absolute}
.topbar{left:0;top:0;width:1030px;height:33px;background:var(--navy)}
.btn{display:flex;align-items:center;justify-content:center;background:var(--orange);color:#fff;font-weight:700;font-size:9px;letter-spacing:.2px;text-transform:uppercase}
.contact-btn{left:128px;top:6px;width:82px;height:22px}
.social{left:225px;top:12px;display:flex;gap:10px;align-items:center}
.social span{width:8px;height:8px;border-radius:50%;background:var(--orange)}
.account{right:130px;top:11px;color:#d6dcea;font-size:9px;display:flex;gap:8px;align-items:center;text-transform:uppercase}
.account i{width:7px;height:8px;background:#9aa7c2;border-radius:2px;display:inline-block;margin-right:3px}
.header{left:0;top:33px;width:1030px;height:59px;background:linear-gradient(#fff,#f2f6fb)}
.brand{left:128px;top:51px;display:flex;align-items:center;gap:8px;font-size:15px;font-weight:700;color:#111;text-transform:uppercase;letter-spacing:.3px}
.brand i{width:10px;height:10px;background:var(--orange);display:block}
.nav{left:399px;top:59px;display:flex;gap:20px;font-size:10px;color:#333;text-transform:uppercase}
.nav .sep{color:#888}
.badge{left:693px;top:50px;width:62px;height:24px;border-radius:12px;background:#2b2f36}
.book-top{left:780px;top:53px;width:121px;height:21px}
.hero{left:0;top:92px;width:1030px;height:391px;background:linear-gradient(180deg,#4f8fd6 0%,#8bb9e8 35%,#5676a6 60%,#2f4c73 80%,#3f6a3a 100%)}
.hero-box{left:156px;top:247px;width:728px;height:105px;background:rgba(13,36,81,.88);color:#fff;text-align:center;padding-top:20px}
.hero-box h1{font-size:26px;font-weight:500;text-transform:uppercase;letter-spacing:-.2px}
.hero-box p{font-size:13px;line-height:16px;margin-top:6px}
.hl{color:var(--orange)}
.sec-title{left:0;width:1030px;text-align:center;top:546px;font-size:25px;font-weight:500;text-transform:uppercase;color:#222}
.card{top:622px;width:249px;height:237px;border:1px solid var(--line);background:#fff;padding:106px 19px 0;text-align:justify;text-align-last:center;font-size:10px;line-height:12.2px;color:var(--muted)}
.card svg{position:absolute;left:50%;top:36px;transform:translateX(-50%)}
.band{left:0;top:907px;width:1023px;height:292px;background:var(--band)}
.skyline{left:487px;top:1095px;width:430px;height:104px}
.frame{border:1px solid #c6ccd6}
.photo{border:0}
.band-frame{left:128px;top:951px;width:284px;height:199px}
.band-photo{left:135px;top:958px;width:284px;height:199px;background:linear-gradient(180deg,#5d9be0 0%,#a9cdee 35%,#5b7ea0 60%,#4f7a3d 85%,#8b8f7f 100%)}
.h2{font-size:25px;font-weight:500;text-transform:uppercase;color:#333;line-height:30px}
.covered-h{left:495px;top:965px}
.body-text{font-size:10.5px;line-height:15px;color:var(--muted);text-align:justify}
.covered-p{left:497px;top:1004px;width:405px}
.fees-h{left:127px;top:1250px}
.fees-p{left:127px;top:1322px;width:404px}
.fees-frame{left:610px;top:1256px;width:284px;height:199px}
.fees-photo{left:617px;top:1263px;width:284px;height:199px;background:linear-gradient(160deg,#f3f3f1 0%,#dedcd8 45%,#8a8a8c 70%,#2d3035 100%)}
.cta{left:0;top:1509px;width:1030px;height:107px;background:var(--navy);text-align:center;color:#fff}
.cta h3{font-size:21px;font-weight:500;text-transform:uppercase;margin-top:28px}
.cta-btn{left:455px;top:59px;width:121px;height:22px}
.foot-links{left:0;width:1030px;top:1650px;text-align:center;font-size:10.5px;color:#333;text-transform:uppercase;word-spacing:2px}
.foot-info{left:0;width:1030px;text-align:center;font-size:10.5px;color:#222}
.foot-info .lbl{color:var(--orange)}
.legal{left:0;top:1732px;width:1030px;height:28px;background:var(--orange);color:#fff;font-size:8.5px;display:flex;align-items:center;justify-content:center;text-transform:uppercase}
</style>
</head>
<body>
<div class="page">
  <div class="abs topbar"></div>
  <div class="abs btn contact-btn">Contact us</div>
  <div class="abs social"><span></span><span></span><span></span></div>
  <div class="abs account"><span><i></i>My account</span><span>|</span><span>Log out</span></div>

  <div class="abs header"></div>
  <div class="abs brand"><i></i>Corvane Hollis</div>
  <nav class="abs nav"><span>Property search</span><span class="sep">|</span><span>Discover</span><span class="sep">|</span><span>About</span></nav>
  <div class="abs badge"></div>
  <div class="abs btn book-top">Book valuation now</div>

  <div class="abs hero" role="img" aria-label="Modern glass office building under a blue sky with trees in front"></div>
  <div class="abs hero-box">
    <h1>Do you think your <span class="hl">business rates</span> are too <span class="hl">high</span>?</h1>
    <p>Use our free valuation tool below or book a valuation with one of our qualified surveyors.<br>No shock commissions and fair fixed fees from <span class="hl">£295!</span></p>
  </div>

  <h2 class="abs sec-title">A better understanding of <span class="hl">your rates</span> payments</h2>

  <div class="abs card" style="left:128px">
    <svg width="66" height="52" viewBox="0 0 66 52" fill="none" stroke-width="2">
      <circle cx="17" cy="14" r="12" stroke="var(--orange)"/>
      <line x1="8" y1="23" x2="2" y2="30" stroke="var(--orange)"/>
      <rect x="16" y="12" width="36" height="24" stroke="var(--orange)"/>
      <line x1="34" y1="36" x2="34" y2="42" stroke="var(--orange)"/>
      <line x1="26" y1="43" x2="42" y2="43" stroke="var(--orange)"/>
      <rect x="48" y="4" width="16" height="44" rx="2" stroke="var(--navy)"/>
    </svg>
    We pride ourselves on working collaboratively with our clients. That's why we offer a free online valuation tool which will help you better understand your rateable valuation and rates payable. We advise checking the factual data shown on the Summary Valuation Breakdown with what is actually on the ground at your property, measuring it at all floor levels, noting the size and any other property features.
  </div>
  <div class="abs card" style="left:391px">
    <svg width="64" height="50" viewBox="0 0 64 50" fill="none" stroke-width="2">
      <path d="M30 8H4v40h34V24" stroke="var(--navy)"/>
      <path d="M20 34l3-9 20-20 6 6-20 20z" stroke="var(--orange)"/>
      <line x1="10" y1="40" x2="32" y2="40" stroke="var(--orange)"/>
      <path d="M56 4v6M53 7h6M50 16v4M48 18h4" stroke="var(--navy)"/>
    </svg>
    Use our free valuation tool to estimate the rateable value of your commercial property in England and Wales. You can add, remove or alter the property information, make allowances and set the base rate pricing. At the end we will provide an estimate of the amount of rates payable and any potential savings.
  </div>
  <div class="abs card" style="left:652px">
    <svg width="50" height="50" viewBox="0 0 50 50" fill="none" stroke-width="2">
      <rect x="2" y="6" width="46" height="42" rx="3" stroke="var(--orange)"/>
      <line x1="2" y1="16" x2="48" y2="16" stroke="var(--orange)"/>
      <path d="M12 2v8M38 2v8" stroke="var(--orange)"/>
      <path d="M10 24h6M20 24h6M30 24h6M40 24h4M10 32h6M20 32h6M30 32h6M40 32h4M10 40h6M20 40h6M30 40h6" stroke="var(--navy)"/>
    </svg>
    Need help? Book a qualified surveyor to advise you on the rateable value of your commercial property. You can book an essential desktop based valuation or a detailed on-site valuation. Our surveyors are not driven by high commissions and will give you an honest fair assessment of your rateable valuation, rates payable and advise you on whether you should commence the Check, Challenge and Appeal process.
  </div>

  <div class="abs band"></div>
  <svg class="abs skyline" viewBox="0 0 430 104" fill="#e2e9f3" aria-hidden="true">
    <rect x="10" y="50" width="20" height="54"/><rect x="40" y="60" width="14" height="44"/><rect x="80" y="20" width="22" height="84"/>
    <rect x="120" y="30" width="26" height="74"/><rect x="160" y="55" width="30" height="49"/><rect x="200" y="40" width="18" height="64"/>
    <rect x="230" y="25" width="22" height="79"/><rect x="265" y="10" width="18" height="94"/><rect x="295" y="30" width="26" height="74"/>
    <rect x="335" y="50" width="20" height="54"/><rect x="370" y="35" width="16" height="69"/><rect x="400" y="45" width="22" height="59"/>
  </svg>
  <div class="abs frame band-frame"></div>
  <div class="abs photo band-photo" role="img" aria-label="Modern glass office campus with a paved walkway and trees"></div>
  <h2 class="abs h2 covered-h">We've got <span class="hl">you</span> covered!</h2>
  <p class="abs body-text covered-p">Our rating list contains the most up-to-date information of around 2 million commercial properties in England and Wales. Our qualified rating surveyors provide nationwide coverage and we employ some of the highest qualified surveyors with some holding the Kestrel Institute Rating Diploma.</p>

  <h2 class="abs h2 fees-h">Fair fixed fees and no shock<br><span class="hl">commissions!</span></h2>
  <div class="abs fees-p">
    <p class="body-text">Our fees are fixed up front, ensuring there are no surprises and we promise to never charge any shock commissions. Not only does this provide you with certainty of cost, it also provides you with confidence that our surveyors are not lead by the prospect of large commission payments. We are here from initial point of contact right through to the end, be that to provide an essential desktop valuation, on-site valuation or helping you through the Check, Challenge and Appeal process. Were here to support and guide you every step of the way.</p>
    <p class="body-text" style="margin-top:15px">Our surveyors don't do speculative appeals, we provide honest and professional advice at a fair fixed fee.</p>
  </div>
  <div class="abs frame fees-frame"></div>
  <div class="abs photo fees-photo" role="img" aria-label="Hand working on a desk calculator beside paperwork"></div>

  <div class="abs cta">
    <h3>Book a rateable valuation with one of our qualified surveyors</h3>
    <div class="abs btn cta-btn">Book valuation now</div>
  </div>

  <div class="abs foot-links">Pricing plans &nbsp;|&nbsp; FAQs &nbsp;|&nbsp; Contact &nbsp;|&nbsp; Legal &amp; terms</div>
  <div class="abs foot-info" style="top:1673px"><span class="lbl">Company Registered Address:</span> Arden House, Quayside Park, Leeds LS9 4TR</div>
  <div class="abs foot-info" style="top:1691px"><span class="lbl">Company Registration Number:</span> 10457732</div>
  <div class="abs legal">© 2019 All rights reserved.</div>
</div>
</body>
</html>
```